SKYVANTEX (drone photo and video) and Photogrammetry Services (mapping and 3D modeling)

We need a business card design for a SKYVANTEX. Our businesses provides (drone) Aerial Photo and Video Captures. However we also provide Photogrammetry (which is 3D modeling and mapping). We greatly value unique points of view taken of landscapes and subjects with aerial photography and videography. 3D modeling and mapping is the other area of focus and have an incredibly broad scope of applications and imaginative creativity.

Target Market(s)

Based out of Northern Virginia and serving the greater Virginia and Maryland areas

Industry/Entity Type

Drone Photo and video and Photogrammetry Services (mapping and 3D modeling)

Contact Information for Business Card

3D Models, Maps and Photo/Video Production name: Marcus Pettibone email: mqp@skyvantex.us website: skyvantex.us phone: 571-806-3394; please also include "Aerial Photo/Video and 3D Mapping/Modeling"

Requirements
Must have
• Please make this design vertical and double sided. The selection box is not letting me choose Double Sided but that is my wish. Incorporate uploaded LOGO and color scheme
Nice to have
• Preferably does not feel too crowded and balances not having an exaggerated amount of distracting detail
Should not have
• do not cram bullet points or text in long form

```html
<!DOCTYPE html>
<html lang="en">
<head>
<meta charset="utf-8">
<title>SKYVANTEX Business Card</title>
<link rel="stylesheet" href="https://fonts.googleapis.com/css2?family=Lato:wght@400;700;900&display=swap">
<style>
  :root {
    --stage: #7f7f7f;
    --card: #ffffff;
    --navy: #232b35;
    --navy-soft: #2e3844;
    --ink: #141414;
    --sun-top: #fbb02d;
    --sun-mid: #f86a2b;
    --sun-bottom: #f0202a;
    --light: #ffffff;
  }
  * { box-sizing: border-box; margin: 0; padding: 0; }
  html, body {
    width: 1200px; height: 875px; overflow: hidden;
    background: var(--stage);
    font-family: "Lato", sans-serif;
  }
  .stage {
    position: relative; width: 1200px; height: 875px;
  }
  .card {
    position: absolute;
    background: var(--card);
    border-radius: 22px;
    overflow: hidden;
    box-shadow: 0 18px 40px rgba(0,0,0,0.35);
  }
  /* Front: portrait */
  .card--front {
    left: 110px; top: 137px; width: 350px; height: 600px;
  }
  .brand {
    position: absolute; left: 34px; top: 52px;
    display: flex; align-items: center; gap: 14px;
  }
  .brand__dot {
    width: 58px; height: 58px; border-radius: 50%;
    background: var(--sun-mid);
  }
  .brand__name {
    font-weight: 900; font-size: 34px; letter-spacing: 1px;
    color: var(--ink);
  }
  .scene-art {
    position: absolute; left: 0; top: 150px; width: 350px; height: 190px;
    background: linear-gradient(180deg, #ffffff 0%, #c9ced4 45%, var(--navy) 100%);
  }
  .contact-panel {
    position: absolute; left: 0; top: 340px; width: 350px; height: 260px;
    background: var(--navy);
    color: var(--light);
    display: flex; flex-direction: column; align-items: center;
    padding-top: 44px;
  }
  .contact-panel__name {
    font-weight: 700; font-size: 25px; letter-spacing: 0.5px;
    text-transform: uppercase;
  }
  .contact-panel__rule {
    width: 18px; height: 2px; background: var(--light);
    margin: 16px 0 18px;
  }
  .contact-panel__phone {
    font-weight: 700; font-size: 19px; margin-bottom: 10px;
  }
  .contact-panel__line {
    font-weight: 400; font-size: 17px; margin-bottom: 6px;
  }
  /* Back: landscape */
  .card--back {
    left: 540px; top: 262px; width: 600px; height: 350px;
  }
  .back-brand {
    position: absolute; left: 0; right: 0; top: 92px;
    display: flex; flex-direction: column; align-items: center; gap: 18px;
  }
  .back-brand__dot {
    width: 96px; height: 96px; border-radius: 50%;
    background: var(--sun-mid);
  }
  .back-brand__name {
    font-weight: 900; font-size: 36px; letter-spacing: 2px; color: var(--ink);
  }
  .tagline {
    position: absolute; left: 0; right: 0; bottom: 34px;
    text-align: center;
    font-weight: 700; font-size: 15px; letter-spacing: 1.2px;
    color: var(--ink); text-transform: uppercase;
  }
</style>
</head>
<body>
<main class="stage">
  <section class="card card--front" aria-label="Card front">
    <div class="brand">
      <span class="brand__dot" aria-hidden="true"></span>
      <span class="brand__name">SKYVANTEX</span>
    </div>
    <div class="scene-art" role="img" aria-label="Mountain range silhouette with a drone flying over the peaks"></div>
    <div class="contact-panel">
      <p class="contact-panel__name">Marcus Pettibone</p>
      <span class="contact-panel__rule" aria-hidden="true"></span>
      <p class="contact-panel__phone">571-806-3394</p>
      <p class="contact-panel__line">mqp@skyvantex.us</p>
      <p class="contact-panel__line">skyvantex.us</p>
    </div>
  </section>

  <section class="card card--back" aria-label="Card back">
    <div class="back-brand">
      <span class="back-brand__dot" aria-hidden="true"></span>
      <span class="back-brand__name">SKYVANTEX</span>
    </div>
    <p class="tagline">Aerial Photo / Video &amp; 3D Mapping / Modeling</p>
  </section>
</main>
</body>
</html>
```